Web design for software company

I'm a software developer that designs high end specialist web applications, mobile apps and user friendly applications for medium to large customers. I integrate different systems together within a company and provide web based applications or mobile apps to view and edit information in that web of linked systems.

I currently work alone, basically selling my time on specialist projects, but also build my own software solutions which I eventually want to put into the market.

My company name is Overthread (lowercase 'L' for logic) and I work from the Netherlands. I've attached my current logo which is basically just text in VOXbox font. Current colours are mustard yellow and grey, but i'm open to other options to better fit the web design.

I've got a sort of slogan: "Specialized software development" - better ideas are welcome. The slogan in the logo attachment is older.

I'm looking for a site design that reflects my work as being on the cutting edge of technology, but being clear and simple. My thinking with the name Overthread is that it refers to the underlying mechanism and logic of software.

The site will not be text heavy, so some kind of large graphic to do with software design is welcome. I expect about 4 or 5 main pages or sections of the site in which i'll eventually add things like a blog or contact info etc.

Industry/Entity Type

It Company

Number of Pages Required

1 page

Font styles to use
Sans Serif

Requirements
Nice to have
• A large graphic or photo relevant to my focus as a software developer. Something that shows connecting of software systems with perhaps a variety of devices/browsers that would display data from that cloud of systems.
• Something like these (allthough these are ugly - but the idea is what i mean):
• http://img4.pixvaultimages.example/2000517/22458/i/450/pixvault_224581133-Cloud-computing-user-interface.jpg
• http://business.tamblinet.example/images/modules/mobile-device-policy-design-banner.png
• https://www.pagecraftly.example/images/responsive-web-design.jpg
• http://www.norvexa.example/images/web_apps.png
• https://www.keyportal.example/assets/img/product/web-app@2x.png?v2
Should not have
• Photographs of smiling happy people looking at a screen that make it look like it's a huge business with many offices. I'm a one-man company which could perhaps grow a little bit, but i want to focus on my expertise instead of size.

```html
<!DOCTYPE html>
<html lang="en">
<head>
<meta charset="utf-8">
<title>Overthread — Software Development</title>
<link href="https://fonts.googleapis.com/css2?family=Roboto+Condensed:wght@400;700&family=Open+Sans:wght@400;600;700&display=swap" rel="stylesheet">
<style>
:root{
  --navy:#0d4a73;
  --navy-deep:#0b4470;
  --orange:#f47b20;
  --teal:#15bfc1;
  --text:#6b6b6b;
  --grey-bg:#f1f1f1;
  --white:#ffffff;
}
*{margin:0;padding:0;box-sizing:border-box}
html,body{width:1200px;height:2687px;overflow:hidden}
body{background:var(--white);font-family:"Open Sans",Arial,sans-serif;color:var(--text);position:relative}
.heading{font-family:"Roboto Condensed",Arial,sans-serif}
.accent{color:var(--orange)}

/* header */
.site-header{position:absolute;top:0;left:0;width:1200px;height:103px;display:flex;align-items:center;padding-left:77px}
.brand{display:flex;align-items:center;gap:14px}
.brand-square{width:36px;height:36px;background:var(--teal)}
.brand-name{font-family:"Roboto Condensed",Arial,sans-serif;font-size:34px;color:var(--navy);letter-spacing:1px}
.main-nav{position:absolute;left:466px;top:42px;display:flex;gap:0}
.main-nav a{font-family:"Roboto Condensed",Arial,sans-serif;font-size:17px;color:#8a8a8a;text-decoration:none;text-transform:uppercase;margin-right:54px}
.main-nav a.active{color:var(--teal)}

/* hero */
.hero{position:absolute;top:103px;left:0;width:1200px;height:574px;background:linear-gradient(110deg,#c9d3d8 0%,#e6ecef 40%,#dfe7ea 60%,#b9c8cf 100%)}
.hero-title{position:absolute;right:78px;top:172px;text-align:right;font-family:"Roboto Condensed",Arial,sans-serif;font-weight:700;font-size:46px;line-height:62px;color:var(--navy);text-transform:uppercase}
.btn{display:inline-block;font-family:"Roboto Condensed",Arial,sans-serif;font-weight:700;text-transform:uppercase;color:var(--white);text-align:center}
.hero .btn{position:absolute;right:78px;top:316px;width:175px;height:56px;line-height:56px;font-size:22px;background:var(--orange);border-radius:3px}

/* section titles */
.section-title{position:absolute;left:0;width:1200px;text-align:center;font-family:"Roboto Condensed",Arial,sans-serif;font-size:47px;color:var(--navy);text-transform:uppercase}
.title-pointer{position:absolute;left:360px;width:480px;height:24px}

/* services */
.services{position:absolute;top:677px;left:0;width:1200px;height:451px}
.service{position:absolute;top:176px;width:240px;text-align:center}
.service svg{display:block;margin:0 auto 10px}
.service h3{font-family:"Roboto Condensed",Arial,sans-serif;font-weight:400;font-size:22px;line-height:31px;color:var(--navy)}
.service p{font-size:15px;line-height:25px;margin-top:4px}

/* about */
.about{position:absolute;top:1128px;left:0;width:1200px;height:312px;background:linear-gradient(100deg,#2c5f86 0%,#4a7ea3 45%,#3f7399 70%,#2b5d83 100%)}
.about .section-title{top:37px;color:var(--white)}
.about p{position:absolute;top:101px;left:170px;width:860px;text-align:center;color:var(--white);font-size:15px;line-height:26px}
.about .btn{position:absolute;top:199px;left:512px;width:175px;height:56px;line-height:56px;font-size:22px;background:var(--teal);border-radius:2px}

/* testimonial */
.testimonial{position:absolute;top:1440px;left:0;width:1200px;height:335px;background:var(--grey-bg)}
.testimonial .section-title{top:47px}
.quote-mark{position:absolute;top:116px;left:0;width:1200px;text-align:center;font-family:Georgia,serif;font-weight:700;font-size:58px;line-height:50px;color:var(--teal)}
.testimonial blockquote{position:absolute;top:160px;left:180px;width:840px;text-align:center;font-size:15px;line-height:26px}
.testimonial cite{position:absolute;top:236px;left:0;width:1200px;text-align:center;font-style:normal;font-weight:700;font-size:15px;color:var(--navy)}
.slide-arrow{position:absolute;top:151px}

/* blog */
.blog{position:absolute;top:1775px;left:0;width:1200px;height:583px}
.blog .section-title{top:48px}
.post{position:absolute;top:176px;width:313px;height:344px;border:1px solid #d8d8d8;background:var(--white)}
.post-image{height:167px}
.post h4{font-family:"Roboto Condensed",Arial,sans-serif;font-weight:400;font-size:18px;line-height:25px;color:var(--navy);padding:10px 13px 0}
.post time{display:flex;align-items:center;gap:6px;font-size:13px;color:#8a8a8a;padding:3px 14px 0}
.post p{font-size:14.5px;line-height:25px;padding:4px 14px 0}

/* footer */
.site-footer{position:absolute;top:2358px;left:0;width:1200px;height:329px;background:var(--navy-deep);color:var(--white)}
.footer-col{position:absolute;top:30px}
.footer-col h5{font-family:"Roboto Condensed",Arial,sans-serif;font-weight:400;font-size:22px;margin-bottom:14px}
.footer-brand{display:flex;align-items:center;gap:10px;margin-top:30px}
.footer-brand .brand-square{width:30px;height:30px;background:var(--white)}
.footer-brand .brand-name{color:var(--white);font-size:28px}
.footer-about{font-size:15px;line-height:25px;margin-top:22px;width:235px}
.footer-links a{display:block;color:#8fd3ec;text-decoration:none;font-size:16px;line-height:31.5px}
.footer-links a:first-child{color:var(--white)}
.contact-row{display:flex;gap:10px;font-size:15px;line-height:25px;margin-bottom:9px;color:#8fd3ec}
.contact-row svg{flex:none;margin-top:5px}
.contact-row.phone{color:var(--white);font-weight:700}
.socials{display:flex;gap:17px;margin-top:8px}
.social{width:52px;height:52px;border-radius:50%}
.social.primary{background:var(--orange)}
.social.plain{background:var(--white)}
.newsletter p{font-size:15px;margin-top:-2px}
.email-field{margin-top:14px;width:232px;height:36px;background:#3d6f94;border:1px solid #5d89a8;color:#e7eef3;font-size:14px;padding:0 8px;line-height:34px}
.subscribe{margin-top:18px;width:160px;height:42px;line-height:42px;background:var(--orange);font-family:"Roboto Condensed",Arial,sans-serif;font-size:22px;text-align:center;text-transform:uppercase}
.footer-rule{position:absolute;top:275px;left:77px;width:1045px;height:1px;background:#2f6a94}
.copyright{position:absolute;top:291px;left:0;width:1200px;text-align:center;font-size:15px}
.copyright strong{color:var(--orange);text-transform:uppercase}
</style>
</head>
<body>

<header class="site-header">
  <div class="brand"><span class="brand-square"></span><span class="brand-name">Overthread</span></div>
  <nav class="main-nav">
    <a class="active" href="#">Home</a>
    <a href="#">About</a>
    <a href="#">Services</a>
    <a href="#">Our Work</a>
    <a href="#">News</a>
    <a href="#">Contact</a>
  </nav>
</header>

<section class="hero" role="img" aria-label="Photo of a laptop showing the company name on its screen, beside a tablet and phone on a glass desk">
  <h1 class="hero-title">Cutting Edge Software<br>Custom Designed</h1>
  <a class="btn" href="#">Contact Us</a>
</section>

<section class="services">
  <h2 class="section-title" style="top:66px">Services <span class="accent">We Provide</span></h2>
  <svg class="title-pointer" style="top:133px" viewBox="0 0 480 24"><path d="M0 2 H222 L240 20 L258 2 H480" fill="none" stroke="#e4e4e4" stroke-width="3"/></svg>

  <div class="service" style="left:75px">
    <svg width="76" height="64" viewBox="0 0 76 64">
      <g fill="var(--orange)">
        <circle cx="28" cy="36" r="17"/>
        <g transform="translate(28 36)"><rect x="-5" y="-24" width="10" height="48"/><rect x="-24" y="-5" width="48" height="10"/><rect x="-5" y="-24" width="10" height="48" transform="rotate(45)"/><rect x="-5" y="-24" width="10" height="48" transform="rotate(-45)"/></g>
        <circle cx="57" cy="16" r="10"/>
        <g transform="translate(57 16)"><rect x="-3" y="-15" width="6" height="30"/><rect x="-15" y="-3" width="30" height="6"/><rect x="-3" y="-15" width="6" height="30" transform="rotate(45)"/><rect x="-3" y="-15" width="6" height="30" transform="rotate(-45)"/></g>
        <circle cx="58" cy="47" r="9"/>
        <g transform="translate(58 47)"><rect x="-3" y="-13" width="6" height="26"/><rect x="-13" y="-3" width="26" height="6"/><rect x="-3" y="-13" width="6" height="26" transform="rotate(45)"/><rect x="-3" y="-13" width="6" height="26" transform="rotate(-45)"/></g>
      </g>
      <g fill="#fff"><circle cx="28" cy="36" r="7"/><circle cx="57" cy="16" r="4"/><circle cx="58" cy="47" r="3.5"/></g>
    </svg>
    <h3>Custom Software<br>Development</h3>
    <p>Lorem Ipsum is simply dummy text of the printing and typesetting industry.</p>
  </div>

  <div class="service" style="left:346px">
    <svg width="76" height="64" viewBox="0 0 76 64">
      <rect x="24" y="0" width="30" height="62" rx="5" fill="none" stroke="var(--teal)" stroke-width="4"/>
      <rect x="28" y="10" width="22" height="38" fill="var(--teal)"/>
      <circle cx="39" cy="55" r="3" fill="var(--teal)"/>
    </svg>
    <h3>Mobile Application<br>Development</h3>
    <p>Lorem Ipsum is simply dummy text of the printing and typesetting industry.</p>
  </div>

  <div class="service" style="left:616px">
    <svg width="76" height="64" viewBox="0 0 76 64">
      <path d="M16 56 A14 14 0 0 1 14 28 A18 18 0 0 1 44 16 A16 16 0 0 1 66 34 A11 11 0 0 1 62 56 Z" fill="var(--orange)"/>
    </svg>
    <h3>Cloud&nbsp; Development</h3>
    <p>Lorem Ipsum is simply dummy text of the printing and typesetting industry.</p>
  </div>

  <div class="service" style="left:887px">
    <svg width="76" height="64" viewBox="0 0 76 64">
      <rect x="3" y="2" width="70" height="46" rx="4" fill="var(--orange)"/>
      <rect x="10" y="9" width="56" height="32" fill="#fff"/>
      <rect x="32" y="48" width="12" height="8" fill="var(--orange)"/>
      <rect x="22" y="56" width="32" height="5" rx="2" fill="var(--orange)"/>
    </svg>
    <h3>Systems Integration</h3>
    <p>Lorem Ipsum is simply dummy text of the printing and typesetting industry.</p>
  </div>
</section>

<section class="about" role="img" aria-label="Photo of hands typing on a laptop keyboard under a blue tint">
  <h2 class="section-title">About <span class="accent">Us</span></h2>
  <p>Lorem Ipsum is simply dummy text of the printing and typesetting industry. Lorem Ipsum has been the industry's standard dummy text ever since the 1500s, when an unknown printer took a galley of type and scrambled it to make a type specimen book.</p>
  <a class="btn" href="#">Read More</a>
</section>

<section class="testimonial">
  <h2 class="section-title">What Our <span class="accent">Client Say</span></h2>
  <div class="quote-mark">&ldquo;</div>
  <svg class="slide-arrow" style="left:98px" width="64" height="64" viewBox="0 0 64 64"><circle cx="32" cy="32" r="30" fill="none" stroke="var(--teal)" stroke-width="2"/><path d="M36 20 L26 32 L36 44" fill="none" stroke="#444" stroke-width="2"/></svg>
  <blockquote>Lorem Ipsum is simply dummy text of the printing and typesetting industry. Lorem Ipsum has been the industry's standard dummy text ever since the 1500.</blockquote>
  <cite>- Client Name</cite>
  <svg class="slide-arrow" style="left:1040px" width="64" height="64" viewBox="0 0 64 64"><circle cx="32" cy="32" r="30" fill="none" stroke="var(--teal)" stroke-width="2"/><path d="M28 20 L38 32 L28 44" fill="none" stroke="#444" stroke-width="2"/></svg>
</section>

<section class="blog">
  <h2 class="section-title">See Our <span class="accent">Latest Blog</span></h2>
  <svg class="title-pointer" style="top:116px" viewBox="0 0 480 24"><path d="M0 2 H222 L240 20 L258 2 H480" fill="none" stroke="#e4e4e4" stroke-width="3"/></svg>

  <article class="post" style="left:77px">
    <div class="post-image" role="img" aria-label="Illustration of a glowing phone projecting a cloud of icons" style="background:radial-gradient(circle at 50% 60%,#9fd8ff 0%,#2b7bd6 45%,#0b2f6e 100%)"></div>
    <h4>Lorem Ipsum is simply dummy text of the printing and typesetting industry.</h4>
    <time><svg width="11" height="11" viewBox="0 0 11 11"><rect x="0.5" y="1.5" width="10" height="9" fill="none" stroke="#999"/><rect x="0.5" y="1.5" width="10" height="2.5" fill="#999"/></svg>6 June 2016</time>
    <p>Lorem Ipsum is simply dummy text of the printing and typesetting industry. Lorem Ipsum has been the industry.</p>
  </article>

  <article class="post" style="left:444px">
    <div class="post-image" role="img" aria-label="Photo of a person working on a laptop in a bright office" style="background:linear-gradient(120deg,#e9e4dc 0%,#c7bfb3 50%,#8d8a87 100%)"></div>
    <h4>Lorem Ipsum is simply dummy text of the printing and typesetting industry.</h4>
    <time><svg width="11" height="11" viewBox="0 0 11 11"><rect x="0.5" y="1.5" width="10" height="9" fill="none" stroke="#999"/><rect x="0.5" y="1.5" width="10" height="2.5" fill="#999"/></svg>6 June 2016</time>
    <p>Lorem Ipsum is simply dummy text of the printing and typesetting industry. Lorem Ipsum has been the industry.</p>
  </article>

  <article class="post" style="left:810px">
    <div class="post-image" role="img" aria-label="Photo of hands holding a tablet at a desk" style="background:linear-gradient(120deg,#eef2f4 0%,#cfdbe1 55%,#9fb6c3 100%)"></div>
    <h4>Lorem Ipsum is simply dummy text of the printing and typesetting industry.</h4>
    <time><svg width="11" height="11" viewBox="0 0 11 11"><rect x="0.5" y="1.5" width="10" height="9" fill="none" stroke="#999"/><rect x="0.5" y="1.5" width="10" height="2.5" fill="#999"/></svg>6 June 2016</time>
    <p>Lorem Ipsum is simply dummy text of the printing and typesetting industry. Lorem Ipsum has been the industry.</p>
  </article>
</section>

<footer class="site-footer">
  <div class="footer-col" style="left:79px;top:6px">
    <div class="footer-brand"><span class="brand-square"></span><span class="brand-name">Overthread</span></div>
    <p class="footer-about">Lorem Ipsum is simply dummy text of the printing and typesetting industry. Lorem Ipsum has been the industry's standard dummy text.</p>
  </div>

  <div class="footer-col footer-links" style="left:349px">
    <h5>Useful Links</h5>
    <a href="#">Home</a>
    <a href="#">About</a>
    <a href="#">Services</a>
    <a href="#">Our Work</a>
    <a href="#">News</a>
    <a href="#">Contact</a>
  </div>

  <div class="footer-col" style="left:620px">
    <h5>Get In Touch</h5>
    <div class="contact-row"><svg width="14" height="18" viewBox="0 0 14 18"><path d="M7 0 A7 7 0 0 1 14 7 C14 12 7 18 7 18 C7 18 0 12 0 7 A7 7 0 0 1 7 0 Z" fill="#fff"/><circle cx="7" cy="7" r="2.6" fill="var(--navy-deep)"/></svg><span>Lorem Ipsum is simply<br>dummy text of the printing.</span></div>
    <div class="contact-row phone"><svg width="16" height="16" viewBox="0 0 16 16"><path d="M3 0 L6 4 L4.5 6 C5.5 8 8 10.5 10 11.5 L12 10 L16 13 L14 16 C7 16 0 9 0 2 Z" fill="#fff"/></svg><span>123 456 7890</span></div>
    <div class="contact-row"><svg width="18" height="13" viewBox="0 0 18 13"><rect x="0.75" y="0.75" width="16.5" height="11.5" fill="none" stroke="#fff" stroke-width="1.5"/><path d="M1 1 L9 7 L17 1" fill="none" stroke="#fff" stroke-width="1.5"/></svg><span>info@overthread.example</span></div>
    <div class="socials">
      <span class="social primary" role="img" aria-label="Social network link"></span>
      <span class="social plain" role="img" aria-label="Social network link"></span>
      <span class="social plain" role="img" aria-label="Social network link"></span>
    </div>
  </div>

  <div class="footer-col newsletter" style="left:890px">
    <h5>Newsletter</h5>
    <p>Subscribe to stay on Overthread</p>
    <div class="email-field">Enter Email Id</div>
    <div class="subscribe">Subscribe</div>
  </div>

  <div class="footer-rule"></div>
  <p class="copyright">&copy; <strong>Overthread</strong> - 2016. All Rights Reserved.</p>
</footer>

</body>
</html>
```